Business cards and stationary
Venoki Imaging, llc
Professional
Miriam Colfax. Dana Pruitt
Owners
17 Harrow Lane
Bloomingburg, ny 12721 (Miriam )
52 Willowby Road
New Windsor, NY 12553 ( Dana )
Miriam 914-555-0142. /. Dana 845-555-0197
Juniper41@mailvex.com

```html
<!DOCTYPE html>
<html lang="en">
<head>
<meta charset="utf-8">
<title>Venoki Imaging, llc — Stationery</title>
<link rel="stylesheet" href="https://fonts.googleapis.com/css2?family=Cinzel:wght@500&family=Open+Sans:wght@400;600&display=swap">
<style>
  :root {
    --bg: #ececee;
    --paper: #ffffff;
    --blue: #1f5fa8;
    --blue-deep: #174a86;
    --purple: #7b2d8e;
    --ink: #2a3550;
    --muted: #6a7285;
    --faint: #e9ecf3;
  }
  * { margin: 0; padding: 0; box-sizing: border-box; }
  html, body { width: 1200px; height: 936px; overflow: hidden; background: var(--bg); }
  .canvas { position: relative; width: 1200px; height: 936px; }
  .sheet {
    position: absolute; background: var(--paper); overflow: hidden;
    box-shadow: 0 2px 6px rgba(0,0,0,0.12);
  }
  .sheet svg.swoosh { position: absolute; inset: 0; width: 100%; height: 100%; }
  .brand { position: absolute; text-align: center; color: var(--blue-deep); }
  .brand .dot { display: block; margin: 0 auto; border-radius: 50%; background: var(--purple); }
  .brand .name { font-family: "Cinzel", serif; font-weight: 500; white-space: nowrap; }
  .brand .tag { font-family: "Cinzel", serif; font-weight: 500; color: var(--muted); letter-spacing: 0.18em; white-space: nowrap; border-top: 1px solid var(--muted); display: inline-block; }
  .contact { position: absolute; font-family: "Open Sans", sans-serif; color: var(--muted); }
  .contact li { list-style: none; display: flex; align-items: center; gap: 5px; white-space: nowrap; }
  .contact .ico { width: 7px; height: 7px; border-radius: 50%; background: var(--blue); flex: none; }
  .faint-mark { position: absolute; border-radius: 50%; background: var(--faint); }

  .letterhead { left: 183px; top: 68px; width: 390px; height: 549px; }
  .folder { left: 634px; top: 38px; width: 462px; height: 579px; }
  .card-front { left: 46px; top: 660px; width: 177px; height: 101px; }
  .card-back { left: 46px; top: 779px; width: 177px; height: 104px; }
  .envelope { left: 264px; top: 675px; width: 436px; height: 203px; }
  .envelope-back { left: 738px; top: 675px; width: 429px; height: 203px; }
  .domain { position: absolute; font-family: "Cinzel", serif; color: #fff; letter-spacing: 0.12em; }
  .domain.dark { color: var(--muted); }
</style>
</head>
<body>
<main class="canvas">

  <!-- Letterhead -->
  <section class="sheet letterhead">
    <div class="brand" style="left:22px;top:24px;width:120px;">
      <span class="dot" style="width:14px;height:14px;margin-bottom:5px;"></span>
      <div class="name" style="font-size:11px;">Venoki Imaging, llc</div>
      <div class="tag" style="font-size:5px;padding-top:1px;">Mobile Ultrasound</div>
    </div>
    <ul class="contact" style="left:255px;top:26px;font-size:6px;line-height:11px;">
      <li><span class="ico"></span>914-555-0142</li>
      <li><span class="ico"></span>845-555-0197</li>
      <li><span class="ico"></span>Juniper41@mailvex.com</li>
    </ul>
    <div class="faint-mark" style="left:145px;top:205px;width:90px;height:90px;"></div>
    <svg class="swoosh" viewBox="0 0 390 549" preserveAspectRatio="none" aria-hidden="true">
      <path d="M200 549 C280 520 350 470 390 405 L390 549 Z" fill="var(--purple)"/>
      <path d="M215 549 C290 525 352 478 390 418 L390 470 C360 510 330 535 300 549 Z" fill="var(--blue)"/>
      <path d="M300 549 C330 535 360 510 390 470 L390 549 Z" fill="var(--purple)"/>
    </svg>
  </section>

  <!-- Presentation folder -->
  <section class="sheet folder">
    <svg class="swoosh" viewBox="0 0 462 579" preserveAspectRatio="none" aria-hidden="true">
      <path d="M270 0 C350 15 420 60 462 120 L462 0 Z" fill="var(--purple)"/>
      <path d="M290 0 C365 20 425 70 462 130 L462 75 C440 40 415 15 385 0 Z" fill="var(--blue)"/>
    </svg>
    <div class="brand" style="left:81px;top:228px;width:300px;">
      <span class="dot" style="width:34px;height:34px;margin-bottom:10px;"></span>
      <div class="name" style="font-size:26px;">Venoki Imaging, llc</div>
      <div class="tag" style="font-size:10px;padding-top:2px;">Mobile Ultrasound</div>
    </div>
  </section>

  <!-- Business card front -->
  <section class="sheet card-front">
    <div class="brand" style="left:6px;top:7px;width:80px;">
      <span class="dot" style="width:10px;height:10px;margin-bottom:2px;"></span>
      <div class="name" style="font-size:7px;">Venoki Imaging, llc</div>
      <div class="tag" style="font-size:3.5px;">Mobile Ultrasound</div>
    </div>
    <ul class="contact" style="left:10px;top:52px;font-size:4.5px;line-height:7px;">
      <li style="color:var(--ink);font-weight:600;">Miriam Colfax, Owner</li>
      <li><span class="ico" style="width:4px;height:4px;"></span>914-555-0142</li>
      <li><span class="ico" style="width:4px;height:4px;"></span>Juniper41@mailvex.com</li>
      <li><span class="ico" style="width:4px;height:4px;"></span>17 Harrow Lane</li>
    </ul>
    <svg class="swoosh" viewBox="0 0 177 101" preserveAspectRatio="none" aria-hidden="true">
      <path d="M120 0 L177 0 L177 101 L160 101 C150 60 138 25 120 0 Z" fill="var(--blue)"/>
      <path d="M160 101 C150 60 138 25 120 0 L128 0 C146 28 160 65 168 101 Z" fill="var(--purple)"/>
    </svg>
  </section>

  <!-- Business card back -->
  <section class="sheet card-back">
    <div class="brand" style="left:0;top:30px;width:177px;">
      <span class="dot" style="width:16px;height:16px;margin-bottom:3px;"></span>
      <div class="name" style="font-size:8px;">Venoki Imaging, llc</div>
    </div>
    <div class="domain dark" style="left:0;width:177px;text-align:center;top:88px;font-size:4.5px;">www.venokiimaging.com</div>
  </section>

  <!-- Envelope front -->
  <section class="sheet envelope">
    <div class="brand" style="left:18px;top:22px;width:120px;">
      <span class="dot" style="width:14px;height:14px;margin-bottom:4px;"></span>
      <div class="name" style="font-size:11px;">Venoki Imaging, llc</div>
      <div class="tag" style="font-size:5px;padding-top:1px;">Mobile Ultrasound</div>
    </div>
    <ul class="contact" style="left:22px;top:92px;font-size:5px;line-height:8px;">
      <li>914-555-0142</li>
    </ul>
    <svg class="swoosh" viewBox="0 0 436 203" preserveAspectRatio="none" aria-hidden="true">
      <path d="M300 203 C350 185 395 150 436 110 L436 203 Z" fill="var(--purple)"/>
      <path d="M315 203 C362 186 405 155 436 122 L436 160 C415 180 395 193 375 203 Z" fill="var(--blue)"/>
    </svg>
  </section>

  <!-- Envelope back -->
  <section class="sheet envelope-back">
    <svg class="swoosh" viewBox="0 0 429 203" preserveAspectRatio="none" aria-hidden="true">
      <defs>
        <linearGradient id="flap" x1="0" y1="0" x2="0" y2="1">
          <stop offset="0" stop-color="var(--blue)"/>
          <stop offset="1" stop-color="var(--blue-deep)"/>
        </linearGradient>
      </defs>
      <path d="M0 0 L429 0 L429 72 C300 58 140 58 0 72 Z" fill="url(#flap)"/>
    </svg>
    <div class="domain" style="left:0;width:429px;text-align:center;top:26px;font-size:9px;">www.venokiimaging.com</div>
  </section>

</main>
</body>
</html>
```